R Bawden Consulting Design

Our company is a multi-faceted consulting service in specialized areas such as project management and event management.
I would like the design to utilise the colour green, but be simple and unique in concept.
The design should communicate collaboration, openness, trust, efficiency and professionalism.
We like the idea of cogs in a wheel or other geometric designs.

Target Market(s)

Target market is large corporate manufacturers.

Industry/Entity Type

Wheel

Contact Information for Business Card

R Bawden Consulting
Marlene Bawden
Ph. 0492 654 071
Email. marlyfoster@velmarnet.example.net
Address. 7 Tarrow Ct, Brenfield Vic 3987 Australia

```html
<!DOCTYPE html>
<html lang="en">
<head>
<meta charset="utf-8">
<title>R Bawden Consulting – Business Card</title>
<link rel="stylesheet" href="https://fonts.googleapis.com/css2?family=Open+Sans:wght@400;600&display=swap">
<style>
  :root {
    --page-bg: #e9e9e9;
    --card-dark: #1f1f1f;
    --card-light: #fafafa;
    --brand-green: #1f9e3c;
    --text-grey: #3c3c3c;
    --white: #ffffff;
  }
  * { box-sizing: border-box; margin: 0; padding: 0; }
  html, body {
    width: 1200px; height: 1200px; overflow: hidden;
    background: var(--page-bg);
    font-family: "Open Sans", Arial, sans-serif;
  }
  .sheet {
    width: 1200px; height: 1200px;
    display: flex; flex-direction: column;
    align-items: center; justify-content: center; gap: 70px;
  }
  .card {
    position: relative;
    width: 800px; height: 489px;
    overflow: hidden;
    box-shadow: 0 6px 18px rgba(0,0,0,0.15);
  }

  /* Front */
  .card-front { background: var(--card-dark); }
  .front-rule {
    position: absolute; left: 0; right: 0; top: 205px;
    height: 4px; background: var(--brand-green);
  }
  .front-brand {
    position: absolute; left: 150px; top: 180px;
    display: flex; align-items: center; gap: 14px;
    background: var(--card-dark);
    padding: 0 18px;
  }
  .brand-mark {
    width: 22px; height: 22px; background: var(--brand-green);
  }
  .brand-name {
    font-size: 40px; font-weight: 600; letter-spacing: 0.5px;
    color: var(--brand-green);
    line-height: 1;
  }

  /* Back */
  .card-back { background: var(--card-light); }
  .back-tab {
    position: absolute; left: 0; top: 120px;
    width: 62px; height: 40px; background: var(--brand-green);
  }
  .back-brand {
    position: absolute; left: 92px; top: 118px;
    display: flex; align-items: center; gap: 12px;
  }
  .back-brand .brand-name { font-size: 38px; }
  .name-band {
    position: absolute; left: 330px; right: 0; top: 205px;
    height: 56px; background: var(--brand-green);
    display: flex; align-items: center; padding-left: 34px;
  }
  .person-name {
    font-size: 26px; font-weight: 600; color: var(--white);
  }
  .contact {
    position: absolute; left: 330px; top: 282px;
    color: var(--text-grey); font-size: 21px; line-height: 1.3;
  }
  .address { margin-left: 34px; margin-bottom: 22px; }
  .contact-row {
    display: flex; align-items: center; gap: 12px; margin-bottom: 8px;
  }
  .contact-icon {
    width: 22px; height: 22px; flex: none;
  }
</style>
</head>
<body>
<main class="sheet">
  <section class="card card-front" aria-label="Business card front">
    <div class="front-rule"></div>
    <div class="front-brand">
      <span class="brand-mark"></span>
      <span class="brand-name">R Bawden Consulting</span>
    </div>
  </section>

  <section class="card card-back" aria-label="Business card back">
    <div class="back-tab"></div>
    <div class="back-brand">
      <span class="brand-name">R Bawden Consulting</span>
    </div>
    <div class="name-band">
      <span class="person-name">Marlene Bawden</span>
    </div>
    <div class="contact">
      <p class="address">7 Tarrow Ct, Brenfield Vic 3987<br>Australia</p>
      <div class="contact-row">
        <svg class="contact-icon" viewBox="0 0 22 22" aria-hidden="true">
          <circle cx="11" cy="11" r="11" fill="#1f9e3c"/>
          <rect x="7.5" y="4.5" width="7" height="13" rx="1.2" fill="none" stroke="#fff" stroke-width="1.5"/>
          <line x1="10" y1="15.3" x2="12" y2="15.3" stroke="#fff" stroke-width="1.3"/>
        </svg>
        <span>0492 654 071</span>
      </div>
      <div class="contact-row">
        <svg class="contact-icon" viewBox="0 0 22 22" aria-hidden="true">
          <circle cx="11" cy="11" r="11" fill="#1f9e3c"/>
          <rect x="5" y="7" width="12" height="8.5" fill="none" stroke="#fff" stroke-width="1.4"/>
          <polyline points="5,7 11,12 17,7" fill="none" stroke="#fff" stroke-width="1.4"/>
        </svg>
        <span>marlyfoster@velmarnet.example.net</span>
      </div>
    </div>
  </section>
</main>
</body>
</html>
```